Brave Ladies - Fitness Retreat

Tri Fold Brochure & Double sided A4 version options, see attached mockup.

Target Market: Women 18-50, Asian mainly .

Kovo Fitness Presents - Brave Ladies Fitness Retreats:

Something communicating the spirit of getting fit, being strong, eating healthy and strong sense of the feminine.

Industry/Entity Type

Fitness

```html
<!DOCTYPE html>
<html lang="en">
<head>
<meta charset="utf-8">
<title>Brave Ladies Boot Camp – Bali Retreats</title>
<link rel="stylesheet" href="https://fonts.googleapis.com/css2?family=Anton&family=Open+Sans:wght@400;600&display=swap">
<style>
  :root {
    --backdrop: #d9d8d2;
    --page-black: #151515;
    --tile-line: #2c2c2c;
    --tile-shade: #1d1d1d;
    --title-white: #f2f2f2;
    --title-shadow: #000000;
    --accent-red: #e0262c;
    --text-white: #ffffff;
    --photo-boxing: linear-gradient(160deg, #7fae3c 0%, #3c6b2a 45%, #d66a9c 75%, #4b9cc7 100%);
    --photo-beach: linear-gradient(170deg, #b8c8d4 0%, #8c8a86 40%, #4e4b48 100%);
    --photo-group: linear-gradient(175deg, #cfe3f2 0%, #e9eef0 45%, #b2b0a8 100%);
    --photo-hero: linear-gradient(180deg, #2b2420 0%, #b6866a 30%, #d44a78 48%, #b07a5e 62%, #3a3a40 82%, #1a1a1a 100%);
  }
  * { box-sizing: border-box; margin: 0; padding: 0; }
  html, body {
    width: 1200px; height: 803px; overflow: hidden;
    background: var(--backdrop);
  }
  .brochure-cover {
    position: absolute; left: 345px; top: 41px;
    width: 509px; height: 720px;
    background-color: var(--page-black);
    background-image:
      repeating-linear-gradient(90deg, transparent 0 84px, var(--tile-line) 84px 86px),
      repeating-linear-gradient(0deg, transparent 0 84px, var(--tile-line) 84px 86px),
      radial-gradient(ellipse at 40% 20%, var(--tile-shade), var(--page-black) 70%);
    overflow: hidden;
    font-family: "Open Sans", sans-serif;
  }
  .cover-title {
    position: absolute; left: 36px; top: 70px;
    font-family: "Anton", sans-serif;
    font-size: 46px; line-height: 1; letter-spacing: 0.5px;
    color: var(--title-white);
    text-shadow: 3px 3px 0 var(--title-shadow), 0 0 8px #000;
  }
  .cover-subtitle {
    position: absolute; left: 170px; top: 122px;
    font-family: "Anton", sans-serif;
    font-size: 24px; letter-spacing: 1px;
    color: var(--accent-red);
  }
  .photo { position: absolute; }
  .photo-boxing { left: 24px; top: 300px; width: 108px; height: 200px; background: var(--photo-boxing); }
  .photo-beach  { left: 136px; top: 258px; width: 104px; height: 212px; background: var(--photo-beach); }
  .photo-group  { left: 244px; top: 214px; width: 86px;  height: 214px; background: var(--photo-group); }
  .photo-hero   { left: 300px; top: 170px; width: 209px; height: 430px; background: var(--photo-hero); }
  .contact-block {
    position: absolute; left: 40px;
    color: var(--text-white);
    font-size: 10.5px; line-height: 1.45;
  }
  .contact-block.host { top: 520px; }
  .contact-block.partner { top: 610px; }
  .brand-mark {
    display: flex; align-items: center; gap: 6px;
    font-family: "Open Sans", sans-serif; font-weight: 600;
    font-size: 14px; color: var(--text-white);
    margin-bottom: 6px;
  }
  .brand-square { width: 14px; height: 14px; background: var(--text-white); }
  .brand-circle { width: 16px; height: 16px; border-radius: 50%; border: 1.5px solid var(--text-white); }
</style>
</head>
<body>
  <main class="brochure-cover">
    <h1 class="cover-title">BRAVE LADIES BOOT CAMP</h1>
    <p class="cover-subtitle">BALI RETREATS</p>

    <div class="photo photo-boxing" role="img" aria-label="Photo of women boxing with pink gloves outdoors"></div>
    <div class="photo photo-beach" role="img" aria-label="Photo of women doing exercises on a dark sand beach"></div>
    <div class="photo photo-group" role="img" aria-label="Photo of a group of women training outdoors"></div>
    <div class="photo photo-hero" role="img" aria-label="Photo of a fit woman in a pink sports top standing with hand on hip"></div>

    <section class="contact-block host">
      <div class="brand-mark"><span class="brand-square"></span>KOVO FITNESS</div>
      <p>Email : hello.kovofitness@mail.com</p>
      <p>Mob : +62 811.4020.7315</p>
      <p>www.kovo-fitness.com</p>
    </section>

    <section class="contact-block partner">
      <div class="brand-mark"><span class="brand-circle"></span>TIDE HOUSE</div>
      <p>Email : info@tidehouse.com</p>
      <p>Mob : +62 811 2049 8860</p>
      <p>www.tidehouse.com</p>
    </section>
  </main>
</body>
</html>
```